LMVBeacon online header

We need a header for our online internal company newsletter/blogsite. It is called the LMVBeacon which is a contraction between LMV (the department associated) and the word Gazette.
We want to have a new modern design for the header that should say "LMVBeacon" or "LMVBeacon online" (there used to be a paper version) in a nice artistic modern friendly inviting way. Sort of like a newspaper header.
There could be an optional text line that says "All the news you need" or something like that.
Target Market(s)
Consulting professionals in the area of mathematics, econometrics and IT
Industry/Entity Type
It Company
Logo Text
LMVBeacon
Colors
Designer to choose colors to be used in the design.
Look and feel

```html
<!DOCTYPE html>
<html lang="en">
<head>
<meta charset="utf-8">
<title>LMVBeacon — All the news you need</title>
<link rel="stylesheet" href="https://fonts.googleapis.com/css2?family=Roboto+Condensed:wght@300;700&display=swap">
<style>
  :root {
    --paper: #c3c3c3;
    --paper-light: #cdcdcd;
    --paper-dark: #b4b4b4;
    --band: #5c5c5c;
    --band-dark: #4a4a4a;
    --title-ink: #4e4e4e;
    --tagline-ink: #f4f4f4;
    --emblem-tint: rgba(255, 255, 255, 0.16);
  }
  html, body {
    margin: 0;
    padding: 0;
    overflow: hidden;
    background: var(--paper);
  }
  .masthead {
    position: relative;
    width: 1200px;
    height: 325px;
    overflow: hidden;
    background:
      linear-gradient(90deg,
        rgba(0,0,0,0) 0%, rgba(0,0,0,0.03) 18%, rgba(255,255,255,0.03) 30%,
        rgba(0,0,0,0.04) 47%, rgba(0,0,0,0) 55%, rgba(0,0,0,0.03) 70%,
        rgba(255,255,255,0.03) 84%, rgba(0,0,0,0.02) 100%),
      linear-gradient(180deg, var(--paper-light) 0%, var(--paper) 50%, var(--paper-dark) 100%);
  }
  .masthead__band {
    position: absolute;
    left: 123px;
    width: 952px;
    background: linear-gradient(90deg, var(--band) 0%, var(--band-dark) 25%, var(--band) 50%, var(--band-dark) 75%, var(--band) 100%);
  }
  .masthead__band--top { top: 0; height: 28px; }
  .masthead__band--bottom { top: 310px; height: 15px; }
  .masthead__emblem {
    position: absolute;
    left: 95px;
    top: -65px;
    width: 470px;
    height: 470px;
    border-radius: 50%;
    background: radial-gradient(circle, var(--emblem-tint) 0%, rgba(255,255,255,0.08) 55%, rgba(255,255,255,0) 72%);
  }
  .masthead__title {
    position: absolute;
    left: 130px;
    top: 140px;
    margin: 0;
    font-family: "Roboto Condensed", "Arial Narrow", sans-serif;
    font-weight: 700;
    font-size: 50px;
    line-height: 1;
    letter-spacing: -0.5px;
    color: var(--title-ink);
  }
  .masthead__tagline {
    position: absolute;
    right: 124px;
    top: 157px;
    margin: 0;
    font-family: "Roboto Condensed", "Arial Narrow", sans-serif;
    font-weight: 300;
    font-size: 25px;
    line-height: 1;
    letter-spacing: -0.3px;
    color: var(--tagline-ink);
    text-transform: uppercase;
  }
</style>
</head>
<body>
  <header class="masthead">
    <div class="masthead__band masthead__band--top"></div>
    <div class="masthead__emblem" role="img" aria-label="Faint embossed circular dial decoration behind the title"></div>
    <h1 class="masthead__title">LMVBeacon</h1>
    <p class="masthead__tagline">All the news you need</p>
    <div class="masthead__band masthead__band--bottom"></div>
  </header>
</body>
</html>
```